Wine Bottle Label Graphic Design (mini bottle 187ml)

Looking for a contemporary custom wine label design for party favors. Inspiration photos provided. **Please see "wine favorite" example in uploads.

Artwork 2.5" wide by 2.75" tall to be placed on 3"x3" stickers. Specs from printer attached but I still want image to fit within the artwork size I specified. Please make label center justified. This is for BOYS. It does not need to be super "masculine"...but definitely not feminine.

Required elements:

Colors: white background, include gold and purple to match logo. Other colors are fine to include.

Name: Toviah 13 (I like use of the No) as shown in the sample, but not required
Varietal: Mitzvah Blend 6.11.2021
Vineyard: Brockel Family Vineyard
Location: Maryland
Logo: See attached (KRNotecard Final)

Serif
Sans Serif

• All the above elements. Clean and crisp design. Contemporary and classy. Purple, Gold, Black colors. See logo. You CAN include cursive font for select elements. I don't mind a combination of print and script.
• Floral, scrolling, background image, old fashioned

```html
<!DOCTYPE html>
<html lang="en">
<head>
<meta charset="utf-8">
<title>Toviah 13 – Mitzvah Blend Labels</title>
<link rel="stylesheet" href="https://fonts.googleapis.com/css2?family=Abril+Fatface&family=Libre+Caslon+Text:wght@400;700&family=Montserrat:wght@500;700&family=Yellowtail&display=swap">
<style>
  :root {
    --purple: #463082;
    --purple-deep: #3a2570;
    --gold-light: #f6df8a;
    --gold: #d9ad3c;
    --gold-dark: #b98a22;
    --ink: #141414;
    --paper: #ffffff;
    --backdrop: #ece7df;
  }
  html, body {
    margin: 0;
    padding: 0;
    overflow: hidden;
  }
  body {
    width: 1068px;
    height: 1200px;
    background: var(--backdrop);
    position: relative;
  }
  .label {
    position: absolute;
    top: 300px;
    width: 490px;
    height: 540px;
    background: var(--paper);
    border-radius: 8px;
    overflow: hidden;
    box-shadow: 0 6px 18px rgba(0,0,0,0.12);
    text-align: center;
  }
  .label--classic { left: 24px; }
  .label--modern { left: 554px; border-radius: 4px; }

  .line { position: absolute; left: 0; right: 0; width: 100%; margin: 0; }

  /* logo stand-in */
  .brand-mark {
    position: absolute;
    left: 50%;
    width: 176px;
    height: 176px;
    margin-left: -88px;
    border-radius: 50%;
    background: var(--purple);
    display: flex;
    align-items: center;
    justify-content: center;
  }
  .brand-mark__name {
    font-family: "Libre Caslon Text", serif;
    font-weight: 700;
    font-size: 19px;
    letter-spacing: 0.08em;
    color: var(--gold-light);
    text-transform: uppercase;
    line-height: 1.25;
  }

  /* classic label */
  .classic__band {
    position: absolute; top: 0; left: 0; right: 0; height: 116px;
    background: var(--purple);
  }
  .classic__gold-stripe {
    position: absolute; top: 116px; left: 0; right: 0; height: 12px;
    background: linear-gradient(90deg, var(--gold-light), var(--gold), var(--gold-light), var(--gold-dark));
  }
  .label--classic .brand-mark { top: 28px; border: 5px solid var(--gold); margin-left: -93px; }
  .classic__title {
    top: 232px;
    font-family: "Abril Fatface", serif;
    font-size: 58px;
    color: var(--ink);
    letter-spacing: 0.01em;
  }
  .classic__varietal {
    top: 336px;
    font-family: "Libre Caslon Text", serif;
    font-weight: 700;
    font-size: 18px;
    letter-spacing: 0.38em;
    color: var(--purple);
  }
  .classic__year {
    top: 376px;
    font-family: "Libre Caslon Text", serif;
    font-size: 14px;
    letter-spacing: 0.3em;
    color: var(--ink);
  }
  .classic__vineyard {
    top: 422px;
    font-family: "Libre Caslon Text", serif;
    font-size: 15px;
    letter-spacing: 0.2em;
    color: var(--purple);
  }
  .classic__region {
    top: 458px;
    font-family: "Libre Caslon Text", serif;
    font-size: 10px;
    letter-spacing: 0.35em;
    color: var(--ink);
  }
  .classic__rule {
    position: absolute; top: 478px; left: 0; right: 0; height: 11px;
    background: var(--purple);
  }
  .classic__gold-band {
    position: absolute; top: 494px; left: 0; right: 0; bottom: 0;
    background: linear-gradient(100deg, var(--gold-light), var(--gold) 35%, var(--gold-light) 55%, var(--gold-dark));
  }

  /* modern label */
  .modern__pattern {
    position: absolute; left: 0; right: 0; height: 32px;
    background: linear-gradient(90deg, var(--gold-light), var(--gold), var(--gold-light), var(--gold-dark));
  }
  .modern__pattern--top { top: 0; }
  .modern__pattern--bottom { bottom: 0; height: 52px; }
  .modern__rule {
    position: absolute; left: 0; right: 0; height: 6px;
    background: var(--purple);
  }
  .modern__rule--top { top: 32px; }
  .modern__rule--bottom { top: 478px; height: 10px; }
  .modern__title {
    top: 62px;
    font-family: "Abril Fatface", serif;
    font-size: 50px;
    color: var(--purple);
    letter-spacing: 0.02em;
  }
  .label--modern .brand-mark { top: 142px; box-shadow: 0 0 0 6px var(--gold); }
  .modern__varietal {
    top: 340px;
    font-family: "Montserrat", sans-serif;
    font-weight: 700;
    font-size: 25px;
    letter-spacing: 0.16em;
    color: var(--purple-deep);
  }
  .modern__year {
    top: 376px;
    font-family: "Montserrat", sans-serif;
    font-weight: 500;
    font-size: 14px;
    letter-spacing: 0.25em;
    color: var(--ink);
  }
  .modern__vineyard {
    top: 412px;
    font-family: "Yellowtail", cursive;
    font-size: 30px;
    color: var(--purple);
  }
  .modern__region {
    top: 452px;
    font-family: "Montserrat", sans-serif;
    font-weight: 700;
    font-size: 12px;
    letter-spacing: 0.4em;
    color: var(--ink);
  }

  .option-mark {
    position: absolute;
    top: 868px;
    width: 490px;
    text-align: center;
    font-family: "Libre Caslon Text", serif;
    font-weight: 700;
    font-size: 24px;
    color: var(--purple);
  }
  .option-mark--a { left: 24px; }
  .option-mark--b { left: 554px; }
</style>
</head>
<body>

  <section class="label label--classic">
    <div class="classic__band"></div>
    <div class="classic__gold-stripe"></div>
    <div class="brand-mark"><span class="brand-mark__name">Kai and<br>Rowan</span></div>
    <p class="line classic__title">TOVIAH 13</p>
    <p class="line classic__varietal">MITZVAH BLEND</p>
    <p class="line classic__year">2021</p>
    <p class="line classic__vineyard">BROCKEL FAMILY VINEYARD</p>
    <p class="line classic__region">MARYLAND</p>
    <div class="classic__rule"></div>
    <div class="classic__gold-band"></div>
  </section>

  <section class="label label--modern">
    <div class="modern__pattern modern__pattern--top" role="img" aria-label="Gold wavy line pattern band"></div>
    <div class="modern__rule modern__rule--top"></div>
    <p class="line modern__title">TOVIAH 13</p>
    <div class="brand-mark"><span class="brand-mark__name">Kai and<br>Rowan</span></div>
    <p class="line modern__varietal">MITZVAH BLEND</p>
    <p class="line modern__year">2021</p>
    <p class="line modern__vineyard">Brockel Family Vineyard</p>
    <p class="line modern__region">MARYLAND</p>
    <div class="modern__rule modern__rule--bottom"></div>
    <div class="modern__pattern modern__pattern--bottom" role="img" aria-label="Gold wavy line pattern band"></div>
  </section>

  <p class="option-mark option-mark--a">A</p>
  <p class="option-mark option-mark--b">B</p>

</body>
</html>
```